bright meridian advisory needs a business card

i need a business card with a logo that will also be used on the website. The company name is "Bright Meridian Advisory"
The business is an advisory and training organisation that specialises in finding a companys 'natural sequence' to success but we will also provide mentoring and counselling to individuals that want to unlock their potential. The process is unique and not full of the normal corporate bullshit so the card should be 'different' and innovative in use of texture, colour, layout etc...I have no guiding principles for you but if you were the head of a new company lloking to make a great first impression what would your card look like? It should have enough of the corporate that the stiffs dont get scared but should be cool enough that the cool kids get it :-)

Target Market(s)

Companies and people looking to grow their staff capabilities. Specialising in IT but can transcend that to other lines of business.

Industry/Entity Type

It Company

Contact Information for Business Card

usuall placeholder stuff Name, Number etc

Requirements
Must have
• cool and innovative logo and use of space
Nice to have
• Background image, subtle use of the caffeine molecule
• A rollable business card similar to the attached image. Would be nice if either side of the card could be half of a DNA helix and by rolling 2 sides together they could connect at one or more points....Perhaps the strands between have a message?
Should not have
• boring usual business card look and feel

```html
<!DOCTYPE html>
<html lang="en">
<head>
<meta charset="UTF-8">
<title>Bright Meridian Advisory – Business Card</title>
<link rel="stylesheet" href="https://fonts.googleapis.com/css2?family=Archivo:wght@700&family=Questrial&display=swap">
<style>
  :root {
    --stage: #e9e6e2;
    --card-white: #ffffff;
    --brand-blue: #1a6fc2;
    --brand-blue-deep: #1565b5;
    --ink: #3a3a3a;
    --rule: #9a9a9a;
    --helix-tint: #6f9fd6;
    --faint: rgba(255, 255, 255, 0.16);
    --white: #ffffff;
  }
  * { margin: 0; padding: 0; box-sizing: border-box; }
  html, body {
    width: 1200px; height: 720px; overflow: hidden;
    background: var(--stage);
  }
  .canvas { position: relative; width: 1200px; height: 720px; }

  .card {
    position: absolute; top: 196px;
    width: 572px; height: 326px;
    overflow: hidden;
    box-shadow: 0 4px 14px rgba(0, 0, 0, 0.18);
  }
  .card--front { left: 20px; background: var(--card-white); }
  .card--back  { left: 606px; background: var(--brand-blue); }

  /* Front */
  .wordmark {
    position: absolute; left: 26px; top: 36px;
    display: flex; align-items: center; gap: 12px;
  }
  .wordmark__square {
    width: 18px; height: 18px; background: var(--brand-blue);
  }
  .wordmark__name {
    font-family: "Archivo", Arial, sans-serif; font-weight: 700;
    font-size: 21px; line-height: 1.08; letter-spacing: 0.5px;
    color: var(--brand-blue); text-transform: uppercase;
  }
  .divider {
    position: absolute; left: 252px; top: 88px;
    width: 1.5px; height: 208px; background: var(--rule);
  }
  .person {
    position: absolute; left: 266px; top: 120px;
    font-family: "Questrial", Arial, sans-serif; color: var(--ink);
  }
  .person__name {
    font-family: "Archivo", Arial, sans-serif; font-weight: 700;
    font-size: 18px; color: var(--brand-blue); letter-spacing: 0.2px;
  }
  .person__title { font-size: 13px; margin-top: 2px; }
  .person__tagline { font-size: 13px; line-height: 1.45; margin-top: 24px; }
  .contact { list-style: none; margin-top: 18px; font-size: 13px; line-height: 1.5; }
  .contact__label { display: inline-block; width: 20px; }

  .helix-band {
    position: absolute; right: 0; top: 56px;
    width: 76px; height: 264px;
    background: linear-gradient(180deg, rgba(26,111,194,0.15), rgba(26,111,194,0.55) 50%, rgba(26,111,194,0.2));
  }

  /* Back */
  .helix-band--faint {
    position: absolute; left: 0; top: 0;
    width: 78px; height: 326px;
    background: linear-gradient(180deg, rgba(255,255,255,0.05), rgba(255,255,255,0.14) 50%, rgba(255,255,255,0.05));
  }
  .molecule-art {
    position: absolute; left: 72px; top: 14px;
    width: 240px; height: 190px; border-radius: 20px;
    background: radial-gradient(ellipse at center, var(--faint), rgba(255,255,255,0) 70%);
  }
  .evolution-art {
    position: absolute; left: 270px; top: 86px;
    width: 276px; height: 116px; border-radius: 16px;
    background: linear-gradient(90deg, rgba(255,255,255,0.06), rgba(255,255,255,0.2));
  }
  .back-name {
    position: absolute; right: 30px; top: 204px;
    text-align: right;
    font-family: "Archivo", Arial, sans-serif; font-weight: 700;
    font-size: 27px; line-height: 1.1; letter-spacing: 1px;
    color: var(--white); text-transform: uppercase;
  }
</style>
</head>
<body>
<main class="canvas">
  <section class="card card--front" aria-label="Card front">
    <div class="wordmark">
      <span class="wordmark__square"></span>
      <p class="wordmark__name">Bright<br>Meridian<br>Advisory</p>
    </div>
    <div class="divider"></div>
    <div class="person">
      <p class="person__name">PERSON NAME</p>
      <p class="person__title">CEO</p>
      <p class="person__tagline">Consectetur adipiscing elit,<br>Donec accumsan.</p>
      <ul class="contact">
        <li><span class="contact__label">P:</span>123 456 7890</li>
        <li><span class="contact__label">E:</span>info@brightmeridian.com</li>
        <li><span class="contact__label">W:</span>www.brightmeridian.com</li>
      </ul>
    </div>
    <div class="helix-band" role="img" aria-label="Half of a striped DNA helix running along the right edge"></div>
  </section>

  <section class="card card--back" aria-label="Card back">
    <div class="helix-band--faint" role="img" aria-label="Faint striped helix strand along the left edge"></div>
    <div class="molecule-art" role="img" aria-label="Faint line drawing of the caffeine molecule"></div>
    <div class="evolution-art" role="img" aria-label="Faint silhouettes showing the stages of human evolution"></div>
    <p class="back-name">Bright<br>Meridian<br>Advisory</p>
  </section>
</main>
</body>
</html>
```